Health & Fitness Author & Public Speaker Needs Visually Stunning Web Design!

We've FINALLY got around to launching a website for Belinda Marchetti - Australian Food Coach and Health & Fitness Expert. The website is to promote her new healthy eating program - "Bright Plate Living".
For a compehensive outline of exactly what we are after, please see the following attached files:
(1) Web Layout (wireframe, content/copy, links to photos to use, sample page we love)
(2) Style Guide (these are the colours, and overall feel we want)
Photos that we'd like used (of Belinda, and food/meals) can be found at these URL's:
Profile: https://www.filecrate.example/sh/q4r8vpl2m7xz/K3tPzWq9Lm
PicVault: https://www.filecrate.example/sh/b7nwe3ju1kd5/9hFrTy2Qxa
HINT:
Before you do ANYTHING - check out this site as it is pretty much EXACTLY what we're after, but with our branding/colours/style: http://tessamorrow.example/
As we will need to revamp our existing Chatterbook page & other printed material, there may be the potential for further work for the successful designer in the future.
Thanks & Good Luck!
Donovan Pryle
Marketing & Business Development Manager
Bright Plate Living
Women, Ages 24 - 45, Interested in Healthly Eating & Fitness
Business

```html
<!DOCTYPE html>
<html lang="en">
<head>
<meta charset="utf-8">
<title>Bright Plate Living</title>
<link href="https://fonts.googleapis.com/css2?family=Ubuntu:wght@400;500;700&family=Open+Sans:ital,wght@0,400;0,600;0,700;1,400&display=swap" rel="stylesheet">
<style>
:root{
  --purple:#93119b;
  --pink:#e8195a;
  --magenta:#c8166e;
  --charcoal:#3a3a3a;
  --page:#ececec;
  --text:#555;
  --white:#fff;
  --line:#d2d2d2;
}
*{box-sizing:border-box;margin:0;padding:0}
html,body{width:890px;height:1200px;overflow:hidden}
body{background:var(--page);font-family:"Open Sans",sans-serif;color:var(--text);position:relative}
.abs{position:absolute}
.header{left:82px;top:0;width:727px;height:81px;background:var(--white);border-bottom:3px solid var(--purple)}
.brand{left:20px;top:26px;display:flex;align-items:center;gap:8px}
.brand-dot{width:14px;height:14px;border-radius:50%;background:var(--pink)}
.brand-name{font-family:"Ubuntu",sans-serif;font-weight:500;font-size:22px;color:var(--purple);letter-spacing:-.3px}
.nav{left:286px;top:37px;width:220px;height:41px}
.nav a{position:absolute;top:0;height:41px;line-height:41px;font-family:"Ubuntu",sans-serif;font-weight:700;font-size:11px;color:var(--purple);text-decoration:none}
.nav .active{left:0;width:56px;text-align:center;background:var(--purple);color:var(--white);padding-top:4px}
.search{left:540px;top:40px;width:172px;height:34px;background:var(--purple);padding:7px 8px}
.search span{display:block;width:134px;height:20px;background:var(--white);font-size:9px;line-height:20px;padding-left:6px;color:var(--purple)}
.search svg{position:absolute;right:8px;top:9px}
.slider{left:85px;top:98px;width:721px;height:284px;background:linear-gradient(90deg,#8a7c70 0%,#b7a99a 35%,#d9d0bf 65%,#cbbfae 100%);box-shadow:0 0 0 4px var(--white),0 10px 14px -6px rgba(0,0,0,.35)}
.slide-copy{left:421px;top:55px;font-family:"Ubuntu",sans-serif;font-weight:700;font-size:19px;line-height:24px;color:var(--purple);white-space:nowrap}
.slide-copy em{display:block;font-family:"Open Sans",sans-serif;font-weight:400;font-size:13px;line-height:20px;color:var(--magenta);margin:0 0 0 4px}
.arrow{top:126px;width:32px;height:36px;background:var(--white);display:flex;align-items:center;justify-content:center}
.dots{right:13px;bottom:17px;display:flex;gap:3px}
.dots i{width:9px;height:9px;background:var(--white);display:block}
.dots i:first-child{background:var(--purple)}
.optin{left:87px;top:413px;width:716px;height:67px;background:var(--white);border:2px solid var(--pink);border-radius:5px;overflow:hidden;box-shadow:0 2px 3px rgba(0,0,0,.15)}
.optin svg{position:absolute;left:0;top:0}
.optin h2{left:22px;top:8px;font-family:"Ubuntu",sans-serif;font-weight:700;font-size:16px;color:var(--white);white-space:nowrap}
.optin p{left:30px;top:31px;width:300px;text-align:center;font-size:10px;line-height:13px;color:var(--white)}
.field{height:22px;border:1px solid #bbb;border-radius:3px;background:var(--white);font-size:10px;line-height:20px;padding-left:6px;color:#999}
.btn-pink{background:var(--pink);color:var(--white);font-family:"Ubuntu",sans-serif;font-weight:700;font-size:10px;text-align:center;line-height:22px;border-radius:2px}
.btn-grey{background:linear-gradient(#f4f4f4,#d8d8d8);border:1px solid #c4c4c4;color:var(--pink);font-family:"Ubuntu",sans-serif;font-weight:700;font-size:10px;text-align:center;border-radius:2px}
.post-title{background:var(--charcoal);color:var(--white);font-family:"Ubuntu",sans-serif;font-weight:700;padding-left:10px;box-shadow:0 2px 2px rgba(0,0,0,.2);white-space:nowrap}
.meta{background:var(--white);border:1px solid var(--line);font-size:8.5px;line-height:13px;color:#333;display:flex;justify-content:space-between;padding:0 8px}
.photo{border:3px solid var(--white);box-shadow:0 0 0 1px var(--line)}
.excerpt{font-size:8.8px;line-height:13.5px;color:#666}
.excerpt b{color:var(--pink);font-weight:700;margin-left:4px}
.side-box{background:var(--white);border:1px solid var(--line)}
.side-head{position:absolute;left:-1px;top:-1px;right:-1px;height:32px;background:var(--charcoal);color:var(--white);font-family:"Ubuntu",sans-serif;font-weight:700;font-size:13.5px;line-height:34px;padding-left:13px}
.side-text{font-size:10px;line-height:16px;color:#333}
.footer{left:82px;top:1159px;width:727px;height:41px;background:var(--purple)}
.footer-links{left:9px;top:0;line-height:41px;font-size:8.5px;color:var(--white)}
.footer-links span{margin:0 6px}
.social{right:8px;top:0;height:41px;display:flex;align-items:center;gap:8px}
.social div{display:flex;align-items:center;gap:3px;font-size:8.5px;font-weight:600;color:var(--white)}
.social i{width:9px;height:9px;background:var(--white);display:block}
</style>
</head>
<body>

<header class="abs header">
  <div class="abs brand"><span class="brand-dot"></span><span class="brand-name">Bright Plate Living</span></div>
  <nav class="abs nav">
    <a class="active" href="#">Home</a>
    <a href="#" style="left:70px">About</a>
    <a href="#" style="left:119px">The Plan</a>
    <a href="#" style="left:185px">Shop</a>
  </nav>
  <div class="abs search">
    <span>Search</span>
    <svg width="16" height="16" viewBox="0 0 16 16"><circle cx="6" cy="6" r="4.3" fill="none" stroke="#fff" stroke-width="2"/><path d="M9.2 9.2l5 5" stroke="#fff" stroke-width="2.6" stroke-linecap="round"/></svg>
  </div>
</header>

<section class="abs slider" role="img" aria-label="Photo of Belinda Marchetti smiling against a weathered plaster wall">
  <div class="abs slide-copy">GET SLIM<br>BOOST ENERGY<br>GUILT FREE<br>WITH BRIGHT PLATE LIVING!<em>With Belinda Marchetti</em></div>
  <div class="abs arrow" style="left:-3px"><svg width="14" height="20"><path d="M12 1L2 10l10 9" fill="none" stroke="#999" stroke-width="2"/></svg></div>
  <div class="abs arrow" style="right:-3px"><svg width="14" height="20"><path d="M2 1l10 9-10 9" fill="none" stroke="#999" stroke-width="2"/></svg></div>
  <div class="abs dots"><i></i><i></i><i></i><i></i></div>
</section>

<section class="abs optin">
  <svg width="716" height="67"><path d="M0 0H375Q345 20 312 67H0Z" fill="#e8195a"/></svg>
  <h2 class="abs">Join the Bright Plate Living Movement!</h2>
  <p class="abs">Get a Weekly serving of Inspiration &amp; Advice that will<br>change your life... Bring It On!</p>
  <div class="abs field" style="left:383px;top:10px;width:148px">Name</div>
  <div class="abs field" style="left:538px;top:10px;width:148px">Email</div>
  <div class="abs btn-pink" style="left:601px;top:38px;width:86px;height:22px">Hook Me Up</div>
</section>

<article>
  <h3 class="abs post-title" style="left:89px;top:502px;width:425px;height:30px;font-size:15px;line-height:30px">Lorem Ipsum Dolor Sit Amet</h3>
  <div class="abs meta" style="left:89px;top:537px;width:425px;height:15px"><span>January 19, 2013</span><span>112 Comments</span></div>
  <div class="abs photo" role="img" aria-label="Green smoothies with kiwi beside a portrait of Belinda" style="left:89px;top:558px;width:425px;height:151px;background:linear-gradient(90deg,#9ccf5a 0%,#e9efe0 35%,#d8cfc5 60%,#6b4a3a 85%,#c9b9aa 100%)"></div>
  <p class="abs excerpt" style="left:93px;top:720px;width:418px">Lorem ipsum dolor sit amet, consectetur adipisicing elit, sed do eiusmod tempor incididunt ut labore et dolore magna aliqua. Ut enim ad minim veniam, quis nostrud exercitation ullamco laboris nisi ut aliquip ex ea commodo consequat. Duis aute irure dolor in reprehenderit in voluptate velit esse cillum dolore eu fugiat nulla pariatur. Excepteur sint occaecat cupidatat non proident, sunt in culpa qui officia deserunt mollit anim id est laborum.<b>Read more</b></p>
</article>

<article>
  <h3 class="abs post-title" style="left:89px;top:826px;width:201px;height:45px;font-size:14px;line-height:18px;padding-top:5px">Sed ut Perspiciatis Unde<br>Omnis Iste Natus</h3>
  <div class="abs meta" style="left:89px;top:876px;width:201px;height:15px"><span>January 18, 2013</span><span>150 Comments</span></div>
  <div class="abs photo" role="img" aria-label="Bowl of green apples, kiwi and broccoli" style="left:89px;top:896px;width:201px;height:149px;background:radial-gradient(circle at 45% 55%,#c7a264 0%,#7fb23e 40%,#2f5a1e 100%)"></div>
  <p class="abs excerpt" style="left:91px;top:1054px;width:198px">Lorem ipsum dolor sit amet, consectetur adipisic-ing elit, sed do eiusmod tempor incididunt ut labore et dolore magna aliqua. Ut enim ad minim veniam, quis nostrud exercitation ullamco laboris nisi ut aliquip consequat.<b>Read more</b></p>
</article>

<article>
  <h3 class="abs post-title" style="left:313px;top:826px;width:201px;height:45px;font-size:14px;line-height:18px;padding-top:6px">At Vero Eos Accusamus<br>Iusto Odio Dignissimos</h3>
  <div class="abs meta" style="left:313px;top:876px;width:201px;height:15px"><span>January 17, 2013</span><span>150 Comments</span></div>
  <div class="abs photo" role="img" aria-label="Salad of mango, avocado and rocket" style="left:313px;top:896px;width:201px;height:149px;background:radial-gradient(circle at 50% 50%,#f0a53a 0%,#8cbf4a 50%,#f2f2ee 100%)"></div>
  <p class="abs excerpt" style="left:315px;top:1054px;width:198px">Lorem ipsum dolor sit amet, consectetur adipisic-ing elit, sed do eiusmod tempor incididunt ut labore et dolore magna aliqua. Ut enim ad minim veniam, quis nostrud exercitation ullamco laboris nisi ut aliquip consequat.<b>Read more</b></p>
</article>

<aside>
  <section class="abs side-box" style="left:557px;top:502px;width:245px;height:228px">
    <h4 class="side-head">Bright Plate Living Guide</h4>
    <div class="abs" role="img" aria-label="Tablet showing the Bright Plate Living eating plan cover" style="left:12px;top:60px;width:110px;height:150px;border-radius:8px;background:linear-gradient(160deg,#2a2a2a,#111);padding:9px">
      <div style="width:100%;height:100%;background:linear-gradient(#f5f0f5 40%,#e46a9a 75%,#b5236b)"></div>
    </div>
    <p class="abs side-text" style="left:133px;top:84px">The <b>ULTIMATE</b><br>Bright Plate<br>Living Guide</p>
    <div class="abs btn-grey" style="left:133px;top:149px;width:98px;height:27px;line-height:25px">Get It Now!</div>
  </section>

  <section class="abs side-box" style="left:557px;top:743px;width:245px;height:199px">
    <h4 class="side-head">12 Week Challenge</h4>
    <div class="abs" role="img" aria-label="Photo of Belinda holding a bunch of grapes" style="left:13px;top:43px;width:113px;height:143px;border:2px solid #fff;box-shadow:0 0 0 1px #d2d2d2;background:linear-gradient(90deg,#9a8c80,#c8bcae)"></div>
    <p class="abs side-text" style="left:137px;top:60px;font-size:9.5px"><b>HEALTHY,<br>HAPPY &amp; HOT</b><br>In No Time Flat!</p>
    <div class="abs btn-grey" style="left:137px;top:115px;width:98px;height:27px;line-height:25px">Join Us Now!</div>
  </section>

  <section class="abs side-box" style="left:557px;top:955px;width:245px;height:185px">
    <h4 class="side-head">Join The Movement!</h4>
    <p class="abs side-text" style="left:16px;top:39px;width:215px;font-size:9.2px">Join the Bright Plate Living Movement and get a free copy of The Fresh Start Kit (valued $27.00)!</p>
    <div class="abs field" style="left:17px;top:80px;width:208px">Name</div>
    <div class="abs field" style="left:17px;top:112px;width:208px">Email</div>
    <div class="abs btn-grey" style="left:75px;top:148px;width:98px;height:27px;line-height:25px">Sign Me Up</div>
  </section>
</aside>

<footer class="abs footer">
  <div class="abs footer-links">Community<span>|</span>Free<span>|</span>Resources<span>|</span>Press<span>|</span>Contact</div>
  <div class="abs social">
    <div><i></i>Chatterbook</div>
    <div><i></i>Chirpline</div>
    <div><i></i>Vidstream</div>
  </div>
</footer>

</body>
</html>
```